Whiskey Bottle Label

I am looking for an image to accompany a whiskey label. I am a Northbrook Pelicans fan and I am going to call my Whiskey Delphine's Red Anchor Whiskey and I need an image. Something that has a fighting cock / rooster theme.

My whiskey will not be for sale, but for gifts to my clients and friends.

```html
<!DOCTYPE html>
<html lang="en">
<head>
<meta charset="utf-8">
<title>Delphine's Red Anchor Whiskey – Label</title>
<link rel="stylesheet" href="https://fonts.googleapis.com/css2?family=Bebas+Neue&family=Cinzel:wght@600&family=Montserrat:wght@400&display=swap">
<style>
  :root {
    --page-bg: #ffffff;
    --label-black: #000000;
    --label-gold: #d8c07a;
    --label-white: #ffffff;
    --caption-grey: #a7aab0;
  }
  html, body {
    margin: 0;
    padding: 0;
    overflow: hidden;
  }
  body {
    width: 1200px;
    height: 980px;
    background: var(--page-bg);
    position: relative;
  }
  .label {
    position: absolute;
    left: 344px;
    top: 170px;
    width: 512px;
    height: 593px;
  }
  .label svg {
    display: block;
  }
  .brand-name {
    font-family: "Cinzel", serif;
    font-weight: 600;
    font-size: 34px;
    fill: var(--label-white);
  }
  .product-line {
    font-family: "Bebas Neue", sans-serif;
    font-size: 116px;
    fill: var(--label-white);
  }
  .origin-text {
    font-family: "Bebas Neue", sans-serif;
    font-size: 30px;
    fill: var(--label-black);
  }
  .caption {
    position: absolute;
    left: 0;
    width: 1200px;
    top: 826px;
    text-align: center;
    font-family: "Montserrat", sans-serif;
    font-size: 26px;
    color: var(--caption-grey);
    margin: 0;
  }
</style>
</head>
<body>
  <div class="label">
    <svg width="512" height="593" viewBox="0 0 512 593" xmlns="http://www.w3.org/2000/svg">
      <defs>
        <radialGradient id="illustration-tone" cx="50%" cy="50%" r="60%">
          <stop offset="0%" stop-color="#d8c07a" stop-opacity="0.75"/>
          <stop offset="70%" stop-color="#d8c07a" stop-opacity="0.25"/>
          <stop offset="100%" stop-color="#000000" stop-opacity="0"/>
        </radialGradient>
        <path id="brand-arc" d="M130,86 Q256,14 382,86"/>
      </defs>

      <rect class="label-body" x="0" y="0" width="512" height="593" rx="40" ry="40" fill="var(--label-black)"/>

      <text class="brand-name" text-anchor="middle">
        <textPath href="#brand-arc" startOffset="50%">DELPHINE’S</textPath>
      </text>

      <rect class="rooster-illustration" x="92" y="92" width="332" height="172"
            fill="url(#illustration-tone)" role="img"
            aria-label="Gold line-art illustration of two fighting roosters facing each other with wings spread"/>

      <g class="divider divider-top" fill="var(--label-gold)" stroke="var(--label-gold)">
        <line x1="84" y1="276" x2="428" y2="276" stroke-width="2"/>
        <circle cx="84" cy="276" r="5" stroke="none"/>
        <circle cx="428" cy="276" r="5" stroke="none"/>
      </g>

      <text class="product-line" x="256" y="372" text-anchor="middle"
            textLength="314" lengthAdjust="spacingAndGlyphs">RED ANCHOR</text>
      <text class="product-line" x="256" y="470" text-anchor="middle"
            textLength="306" lengthAdjust="spacingAndGlyphs">WHISKEY</text>

      <g class="divider divider-bottom" fill="var(--label-gold)" stroke="var(--label-gold)">
        <line x1="84" y1="488" x2="428" y2="488" stroke-width="2"/>
        <circle cx="84" cy="488" r="5" stroke="none"/>
        <circle cx="428" cy="488" r="5" stroke="none"/>
      </g>

      <polygon class="origin-banner" points="148,516 365,516 346,534 365,552 148,552 167,534"
               fill="var(--label-gold)"/>
      <text class="origin-text" x="256" y="546" text-anchor="middle"
            textLength="158" lengthAdjust="spacingAndGlyphs">NORTHBROOK</text>
    </svg>
  </div>
  <p class="caption">Label Design</p>
</body>
</html>
```